Borvel Stake Pool, redesign of existing website

Borvel is a stake pool that allow its users to stake their Marevo crypto to yearn stable yields. The existing site is at www.borvelstake.org The site is today is a little dull and I want to have suggestions for a redesign that makes the site stand out and that picks up the colors of the logo. I am not looking for a complete redesign, mainly colors and smaller changes to layout. Examples of sites to be inspired by www.quenda.network, https://app.tervalo.finance/

Target Market(s)

Crypto users on Marevo

Number of Pages Required

1 page

```html
<!DOCTYPE html>
<html lang="en">
<head>
<meta charset="utf-8">
<title>Borvel Stake</title>
<link rel="stylesheet" href="https://fonts.googleapis.com/css2?family=Poppins:wght@400;500;600;700&family=Roboto+Slab:wght@700&display=swap">
<style>
:root{
  --teal:#0aa88f;
  --teal-blue:#1496c4;
  --orange:#f47322;
  --ink:#1c1c1c;
  --muted:#444;
  --field:#dde3ec;
  --field-label:#9fcfd6;
  --tab-off:#e6e6e6;
  --tab-off-text:#9a9a9a;
  --rule:#b9b9b9;
}
*{box-sizing:border-box;margin:0;padding:0}
html,body{width:1200px;height:865px;overflow:hidden}
body{
  position:relative;
  font-family:"Poppins",sans-serif;
  color:var(--ink);
  background:
    radial-gradient(circle at 0 160px,rgba(150,220,205,.55),transparent 260px),
    radial-gradient(circle at 250px 330px,rgba(200,235,225,.6),transparent 280px),
    radial-gradient(circle at 1110px 480px,rgba(120,215,210,.45),transparent 200px),
    #fff;
}
.abs{position:absolute}
.brand{left:112px;top:22px;display:flex;align-items:center;gap:14px}
.brand-dot{width:58px;height:58px;border-radius:50%;background:var(--teal)}
.brand-name{font-family:"Roboto Slab",serif;font-weight:700;font-size:32px;color:var(--ink)}
.nav{top:42px;font-size:17px;font-weight:500;color:#555}
.nav.active{color:var(--teal)}
.btn{
  display:flex;align-items:center;justify-content:center;
  color:#fff;font-weight:700;letter-spacing:.3px;
  background:linear-gradient(180deg,var(--teal),var(--teal-blue));
  border-radius:3px;box-shadow:0 2px 4px rgba(0,0,0,.15);
}
.select-wallet{left:941px;top:31px;width:147px;height:47px;font-size:15px}
.tab{top:176px;width:130px;height:53px;font-size:17px;font-weight:700;border-radius:2px}
.tab.off{background:var(--tab-off);border:2px solid #bdbdbd;color:var(--tab-off-text);display:flex;align-items:center;justify-content:center}
.apy{left:110px;top:242px;font-size:23px;text-decoration:underline;text-underline-offset:4px}
.field{left:102px;width:433px;height:53px;background:var(--field);border-radius:3px;overflow:hidden}
.field-label{width:163px;height:100%;background:var(--field-label);display:flex;align-items:center;gap:8px;padding-left:14px;font-weight:600;font-size:18px}
.token-dot{width:28px;height:28px;border-radius:50%}
.meta{left:102px;width:433px;display:flex;justify-content:space-between;font-size:16px}
.meta a{color:var(--ink);text-decoration:underline}
.connect{left:102px;top:592px;width:434px;height:54px;font-size:17px}
.notice{
  left:573px;top:137px;width:524px;height:175px;background:var(--orange);
  color:#fff;font-size:16px;font-weight:500;line-height:25px;padding:14px 30px 0 23px;text-align:justify;
  box-shadow:0 2px 5px rgba(0,0,0,.15);
}
.notice b{font-weight:700}
.notice-close{position:absolute;right:9px;top:4px;font-weight:600;font-size:15px}
.intro{left:595px;top:342px;width:472px}
.intro h1{font-family:"Roboto Slab",serif;font-weight:700;font-size:34px;line-height:46px;margin-bottom:8px}
.intro p{font-size:16px;line-height:25px;color:#2a2a2a;text-align:justify;margin-bottom:14px}
.footer-links{left:0;width:1200px;top:718px;text-align:center;font-size:17px;font-weight:500}
.rule{left:111px;top:778px;width:978px;height:1px;background:var(--rule)}
.copy{left:0;width:1200px;top:806px;text-align:center;font-size:16px;color:#333}
.side-badge{left:13px;top:710px;width:43px;height:43px;border-radius:50%;background:#1a2a3a}
.help{left:1113px;top:688px;width:87px;height:62px;background:var(--teal);border-radius:31px 0 0 31px;display:flex;align-items:center;justify-content:center}
</style>
</head>
<body>
<header>
  <div class="abs brand"><span class="brand-dot"></span><span class="brand-name">Borvel Stake</span></div>
  <span class="abs nav active" style="left:656px">Home</span>
  <span class="abs nav" style="left:748px">Validators</span>
  <span class="abs nav" style="left:876px">Docs</span>
  <div class="abs btn select-wallet">SELECT WALLET</div>
</header>

<main>
  <div class="abs btn tab" style="left:102px">STAKE</div>
  <div class="abs tab off" style="left:261px">UNSTAKE</div>
  <div class="abs tab off" style="left:420px">REFERRAL</div>
  <div class="abs apy">Current APY: 8.03% across 60 validators</div>

  <div class="abs field" style="top:336px"><div class="field-label"><span class="token-dot" style="background:#1b1b2b"></span>MRV</div></div>
  <div class="abs meta" style="top:393px"><span>balance: 0 MRV</span><a>max half</a></div>

  <div class="abs field" style="top:453px"><div class="field-label"><span class="token-dot" style="background:#ef5a3c"></span>BORVELMRV</div></div>
  <div class="abs meta" style="top:511px"><span>balance: 0 borvelMRV</span><a>1 borvelMRV ≈ 1.01714 MRV</a></div>

  <div class="abs btn connect">CONNECT WALLET</div>

  <aside class="abs notice"><span class="notice-close">X</span><b>EARN POINTS</b> The Borvel Points Program is live! When you stake on Borvel you earn points. Hold it or earn even more points when using your borvelMRV with our defi partners. The amount of points determines what your allocation will be for our future governance token BRV. Leaderboard will be available soon!</aside>

  <section class="abs intro">
    <h1>Liquid Staking on Marevo</h1>
    <p>Borvel Stake Pool offers non-custodial staking. Stake your MRV to receive a liquid staking token, borvelMRV, that you can use in Defi on Marevo.</p>
    <p>Let us take care of managing your stake across the best validators on Marevo, and your staking rewards will be automatically compounded each epoch. The value of borvelMRV relative to MRV will increase every epoch.</p>
    <p>It is important for us you feel safe when staking with Borvel! Borvel Stake Pool is based on the Marevo Foundation stake pool program that has been audited 9 times.</p>
  </section>
</main>

<footer>
  <div class="abs footer-links">defi | docs | validators | chatterly | birdline</div>
  <div class="abs rule"></div>
  <div class="abs copy">©2024. All rights reserved.</div>
</footer>

<div class="abs side-badge" role="img" aria-label="Partner badge"></div>
<div class="abs help" role="img" aria-label="Help chat">
  <svg width="40" height="34" viewBox="0 0 40 34" fill="none" stroke="#fff" stroke-width="3"><rect x="6" y="6" width="28" height="18" rx="8"/><circle cx="15" cy="15" r="2" fill="#fff"/><circle cx="25" cy="15" r="2" fill="#fff"/><path d="M2 12v6M38 12v6M16 29h8"/></svg>
</div>
</body>
</html>
```